Velorin business card design

Design a business card for a cryptocurrency company that uses the attached logo. Some example business cards to give you guys a flavor of what we're looking for is given below (of course feel free to be creative):
https://www.plumcardhub.example/studio.aspx?template=4819265_KT3&ag=True&xnav=HSG_Design_Image&rd=1
https://www.plumcardhub.example/studio.aspx?template=3027514_KT3&ag=True&xnav=HSG_Design_Image&rd=1
The business card should be clean/simple and convey the company name, what we're about and the specific persons contact info. In terms of what we're about, we can have our name Velorin, with a line under it that says "Cryptocurrency visualization, analytics, and trading"
We want something futuristic looking but simple / clean.
The color scheme for the logo should be used.
The name of the person and their title should be editable, so we can use the business card design for multiple people.
(Please use the zip file to get the vector graphics and different image formats)

```html
<!DOCTYPE html>
<html lang="en">
<head>
<meta charset="utf-8">
<title>Velorin Business Card</title>
<link rel="stylesheet" href="https://fonts.googleapis.com/css2?family=Lato:wght@400;700&display=swap">
<style>
  :root {
    --backdrop: #1a1f2b;
    --card: #ffffff;
    --ink: #3a3a3a;
    --navy: #1b2438;
    --accent-blue: #1a9ad6;
    --mark: #17b3a9;
    --rule: #333333;
  }
  * { margin: 0; padding: 0; box-sizing: border-box; }
  html, body {
    width: 1200px; height: 1200px; overflow: hidden;
    background: var(--backdrop);
    font-family: "Lato", sans-serif;
  }
  .business-card {
    position: absolute; left: 50px; top: 264px;
    width: 1100px; height: 672px;
    background: var(--card);
    color: var(--ink);
  }
  .brand-dot {
    position: absolute; left: 165px; top: 118px;
    width: 240px; height: 240px; border-radius: 50%;
    background: var(--mark);
  }
  .brand-name {
    position: absolute; left: 60px; width: 450px; top: 452px;
    text-align: center;
    font-size: 64px; font-weight: 700; letter-spacing: 4px;
    color: var(--navy); line-height: 1;
  }
  .brand-tagline {
    position: absolute; left: 60px; width: 450px; top: 533px;
    text-align: center;
    font-size: 13px; font-weight: 700; letter-spacing: 0.4px;
    color: var(--navy);
  }
  .details { position: absolute; left: 641px; top: 0; width: 437px; height: 100%; }
  .person-name {
    position: absolute; top: 148px; left: 2px;
    font-size: 32px; line-height: 1; font-weight: 400; color: var(--ink);
  }
  .person-name .first { font-weight: 700; color: var(--accent-blue); }
  .person-title {
    position: absolute; top: 183px; left: 2px;
    font-size: 21px; line-height: 1; color: var(--ink);
  }
  .divider { position: absolute; left: 0; width: 437px; height: 2px; background: var(--rule); }
  .divider.upper { top: 237px; }
  .divider.lower { top: 366px; }
  .company-line {
    position: absolute; top: 284px; left: 2px;
    font-size: 35px; line-height: 1; color: var(--ink);
  }
  .company-line strong { font-weight: 700; }
  .company-address {
    position: absolute; top: 322px; left: 2px;
    font-size: 21px; line-height: 1; color: var(--ink);
  }
  .contact-list { position: absolute; top: 410px; left: 0; list-style: none; }
  .contact-item {
    display: flex; align-items: center; height: 28px;
    font-size: 22px; color: var(--ink);
  }
  .contact-item.gap { margin-top: 18px; }
  .contact-item svg { width: 22px; height: 18px; margin-right: 20px; flex: none; }
</style>
</head>
<body>
  <div class="business-card">
    <div class="brand-dot"></div>
    <div class="brand-name">VELORIN</div>
    <div class="brand-tagline">CRYPTOCURRENCY VISUALIZATION &nbsp;|&nbsp; ANALYTICS &nbsp;|&nbsp; TRADING</div>

    <div class="details">
      <div class="person-name"><span class="first">JOHNATHAN</span> DOE</div>
      <div class="person-title">GRAPHIC DESGINER</div>
      <div class="divider upper"></div>
      <div class="company-line"><strong>BUSINESS CARD</strong> VELORIN</div>
      <div class="company-address">418 Harlow Street, Brookvale 54321</div>
      <div class="divider lower"></div>

      <ul class="contact-list">
        <li class="contact-item">
          <svg viewBox="0 0 22 18"><path d="M1 6c3-5 17-5 20 0l-1 3h-4l-1-3H7L6 9H2z" fill="#333"/><rect x="4" y="10" width="14" height="7" rx="1" fill="#333"/></svg>
          + 000 - 1234 - 5678
        </li>
        <li class="contact-item">
          <svg viewBox="0 0 22 18"><rect x="5" y="0" width="12" height="5" fill="#333"/><rect x="1" y="6" width="20" height="7" rx="1" fill="#333"/><rect x="5" y="12" width="12" height="6" fill="#333"/></svg>
          + 000 - 9876 - 5432
        </li>
        <li class="contact-item gap">
          <svg viewBox="0 0 22 18"><rect x="1" y="2" width="20" height="14" fill="#333"/><path d="M2 3l9 7 9-7" stroke="#fff" stroke-width="1.6" fill="none"/><path d="M2 15l7-6M20 15l-7-6" stroke="#fff" stroke-width="1.2"/></svg>
          admin@businesscardvelorin.com
        </li>
        <li class="contact-item">
          <svg viewBox="0 0 22 18"><rect x="2" y="1" width="18" height="12" fill="none" stroke="#333" stroke-width="2.2"/><rect x="9" y="13" width="4" height="3" fill="#333"/><rect x="6" y="16" width="10" height="2" fill="#333"/></svg>
          businesscardvelorin.com
        </li>
      </ul>
    </div>
  </div>
</body>
</html>
```